Create a flyer design (10cm X 21cm) for an aquarium in France

We are a public aquarium in France and we want announcing the events of christmas holidays
We invite you to create our flyer recto (just the front side).

The size of this flyer is : 10cm X 21cm
Have a look on flyer.doc to know texts...
We want also get the flyer in original version (.psd, .ai) please.

We remain at your disposal for any question.
Thanks.

Industry/Entity Type

Events

Requirements
Must have
• The text must be written in french, you will find attached all the text that you have to fill in the flyer.
• You also have to use our logo in the top or in the bottom of the flyer (2 versions of the logo four color or black and white version. According your design you can use one of them)
• You must specify our website and our adress.
• Have a look on flyer.doc to know texts...

```html
<!DOCTYPE html>
<html lang="fr">
<head>
<meta charset="utf-8">
<title>Vos vacances de Noël à l'Aquarium</title>
<link rel="stylesheet" href="https://fonts.googleapis.com/css2?family=Cinzel:wght@400;600&family=Great+Vibes&family=Crimson+Pro:wght@400;700&display=swap">
<style>
  :root {
    --red: #b3202a;
    --yellow: #fcc419;
    --box-border: #3b2c12;
    --ink: #1d1d1d;
    --white: #ffffff;
    --photo-sea: #2f5a58;
    --photo-deep: #1c3a44;
  }
  * { margin: 0; padding: 0; box-sizing: border-box; }
  html, body { width: 1200px; height: 2520px; overflow: hidden; }
  body { background: var(--red); font-family: "Crimson Pro", Georgia, serif; color: var(--ink); }

  .flyer { position: relative; width: 1200px; height: 2520px; background: var(--red); overflow: hidden; }

  .hero-backdrop {
    position: absolute; left: 0; top: 0; width: 1200px; height: 1076px;
    background: linear-gradient(180deg, #e9e6e6 0%, #dcd3d3 35%, #cfc6c8 60%, #c9b9bb 85%, #b55a60 100%);
  }
  .top-rule { position: absolute; left: 0; top: 0; width: 1200px; height: 10px; background: var(--red); }

  .brand-badge {
    position: absolute; left: 20px; top: 0; width: 240px; height: 150px;
    background: var(--yellow); border-radius: 0 0 28px 28px;
    display: flex; flex-direction: column; align-items: center; justify-content: center;
  }
  .brand-badge .brand-name { font-weight: 700; font-size: 36px; line-height: 1; color: var(--red); text-align: center; }
  .brand-badge .brand-sub { margin-top: 8px; font-size: 17px; color: var(--red); font-weight: 700; letter-spacing: 1px; }

  .headline { position: absolute; left: 300px; top: 34px; width: 800px; text-align: center; }
  .headline .kicker { font-family: "Cinzel", serif; font-size: 62px; color: #111; line-height: 1; }
  .headline .script { font-family: "Great Vibes", cursive; font-size: 170px; color: var(--red); line-height: 0.9; margin-top: 4px; }
  .headline .venue { display: flex; align-items: center; justify-content: center; gap: 24px; }
  .headline .venue span { font-family: "Cinzel", serif; font-size: 74px; color: #111; line-height: 1; }
  .headline .venue i { display: block; width: 110px; height: 4px; background: #111; }

  .intro { position: absolute; left: 0; top: 372px; width: 1200px; text-align: center; }
  .intro .lead { font-weight: 700; font-size: 43px; line-height: 1.18; color: #111; }
  .intro .note { margin-top: 30px; font-size: 32px; line-height: 1.25; color: #222; }

  .event { position: absolute; background: var(--yellow); border: 4px solid var(--box-border); border-radius: 16px;
    display: flex; flex-direction: column; justify-content: center; align-items: center; text-align: center; color: #111; }
  .event .title { font-weight: 700; font-size: 42px; line-height: 1.15; }
  .event .date { font-size: 33px; line-height: 1.3; margin-top: 10px; }
  .event.small .title { font-size: 37px; }
  .event-dive { left: 36px; top: 636px; width: 554px; height: 164px; }
  .event-sharks { left: 612px; top: 636px; width: 552px; height: 164px; }
  .event-night { left: 36px; top: 830px; width: 554px; height: 220px; }
  .event-fish { left: 612px; top: 830px; width: 552px; height: 220px; }

  .photo { position: absolute; border: 8px solid var(--white); background: linear-gradient(160deg, var(--photo-sea), var(--photo-deep)); }
  .photo.warm { background: linear-gradient(160deg, #3f6a5e, #6a3a32); }
  .photo.blue { background: linear-gradient(160deg, #2b4f7a, #14263e); }

  .footer-brand { position: absolute; left: 70px; top: 2322px; width: 240px; font-weight: 700; font-size: 40px; line-height: 1; color: var(--white); text-align: center; }
  .divider { position: absolute; top: 2300px; width: 3px; height: 124px; background: var(--white); }
  .address { position: absolute; left: 372px; top: 2300px; width: 420px; text-align: center; color: var(--white); font-size: 33px; line-height: 1.2; }
  .phone { position: absolute; left: 820px; top: 2326px; width: 360px; text-align: center; color: var(--yellow); font-size: 56px; font-weight: 700; line-height: 1.2; }
  .web { position: absolute; left: 0; top: 2440px; width: 1200px; text-align: center; color: var(--white); font-weight: 700; font-size: 34px; }
</style>
</head>
<body>
<main class="flyer">
  <div class="hero-backdrop" role="img" aria-label="Photo estompée d'un plongeur costumé en rouge dans un bassin de l'aquarium"></div>
  <div class="top-rule"></div>

  <div class="brand-badge">
    <span class="brand-name">Aquarium<br>de Kerlune</span>
    <span class="brand-sub">BAIE DE KERLUNE</span>
  </div>

  <header class="headline">
    <p class="kicker">VOS VACANCES</p>
    <p class="script">de Noël à l’</p>
    <p class="venue"><i></i><span>AQUARIUM</span><i></i></p>
  </header>

  <section class="intro">
    <p class="lead">Animations « bassin tactile »<br>commentées plusieurs fois par jour</p>
    <p class="note">Nourrissages commentés de<br>nos espèces aquatiques chaque après-midi</p>
  </section>

  <div class="event event-dive"><p class="title">Plongée du Capitaine Corail</p><p class="date">les 22 et 23 décembre</p></div>
  <div class="event event-sharks small"><p class="title">Atelier scientifique sur<br>les Requins lundi</p><p class="date">28 décembre</p></div>
  <div class="event event-night small"><p class="title">Nocturne, une visite drôle<br>et décalée,</p><p class="date">mardi 29 décembre</p></div>
  <div class="event event-fish small"><p class="title">Fish manucure, les 29, 30<br>et 31 décembre<br>Dégustation vitaminée,<br>les 2 et 3 janvier</p></div>

  <div class="photo warm" style="left:36px;top:1086px;width:210px;height:310px" role="img" aria-label="Plongeur costumé dans le bassin"></div>
  <div class="photo blue" style="left:264px;top:1086px;width:220px;height:310px" role="img" aria-label="Poisson-lion"></div>
  <div class="photo warm" style="left:500px;top:1086px;width:210px;height:310px" role="img" aria-label="Plongeur costumé parmi les poissons"></div>
  <div class="photo warm" style="left:726px;top:1086px;width:210px;height:310px" role="img" aria-label="Plongeur costumé avec un sac"></div>
  <div class="photo blue" style="left:954px;top:1086px;width:210px;height:310px" role="img" aria-label="Plongeur costumé saluant"></div>

  <div class="photo" style="left:36px;top:1424px;width:358px;height:188px" role="img" aria-label="Poisson-coffre jaune"></div>
  <div class="photo" style="left:420px;top:1424px;width:356px;height:188px" role="img" aria-label="Plongeur costumé devant le public"></div>
  <div class="photo blue" style="left:808px;top:1424px;width:356px;height:188px" role="img" aria-label="Poisson tacheté"></div>

  <div class="photo blue" style="left:36px;top:1644px;width:358px;height:190px" role="img" aria-label="Poissons chirurgiens bleus"></div>
  <div class="photo warm" style="left:420px;top:1644px;width:356px;height:190px" role="img" aria-label="Plongeur costumé avec une pancarte"></div>
  <div class="photo warm" style="left:808px;top:1644px;width:356px;height:190px" role="img" aria-label="Plongeur costumé"></div>

  <div class="photo" style="left:36px;top:1864px;width:358px;height:186px" role="img" aria-label="Poisson tacheté sur le sable"></div>
  <div class="photo warm" style="left:420px;top:1864px;width:356px;height:186px" role="img" aria-label="Plongeur costumé lisant un message"></div>
  <div class="photo blue" style="left:808px;top:1864px;width:356px;height:186px" role="img" aria-label="Poisson-ange bleu et jaune"></div>

  <div class="photo" style="left:36px;top:2084px;width:358px;height:186px" role="img" aria-label="Plongeur costumé dans les coraux"></div>
  <div class="photo blue" style="left:420px;top:2084px;width:356px;height:186px" role="img" aria-label="Poisson-clown"></div>
  <div class="photo blue" style="left:808px;top:2084px;width:356px;height:186px" role="img" aria-label="Poisson-ange jaune et bleu"></div>

  <footer>
    <p class="footer-brand">Aquarium<br>de Kerlune</p>
    <span class="divider" style="left:346px"></span>
    <p class="address">Aquarium de Kerlune<br>14, rue des Goélands<br>56990 KERLUNE</p>
    <span class="divider" style="left:808px"></span>
    <p class="phone">02 00 48 21 37</p>
    <p class="web">Retrouvez toutes les informations via aquariumdekerlune.fr</p>
  </footer>
</main>
</body>
</html>
```